Business Card Design for BrightlaneReach.com

--I need a business card design for my company BrightlaneReach.com

I have attached my logo...I want the brightlane reach logo on the front of the business card, and then I want The Brightlane Chief on the back of it with my information.

I would like to see a light colored background as well as a dark colored background

FRONT:
BRIGHTLANE REACH LOGO
247 E. Pelham Row
5th Floor
San Diego CA 92384
www.BrightlaneReach.com

Advanced Website & App Development
Websites, Apps, Online Voucher Systems

Leading Edge Marketing Services
SMS, VB, SMM, SEM,

BACK:
BRIGHTLANE CHIEF LOGO
Dorian Welker
The Brightlane Chief
Call Or Text: 555-204-3378
Dorian@BrightlaneChief.com
www.BrightlaneChief.com

Target Market(s)

small business owners

Industry/Entity Type

Business Consultant

Contact Information for Business Card

FRONT:
BRIGHTLANE REACH LOGO
247 E. Pelham Row
5th Floor
San Diego CA 92384
www.BrightlaneReach.com

SMS, VB, SMM, SEM,

BACK:
BRIGHTLANE CHIEF LOGO
Dorian Welker
The Brightlane Chief
Dorian@BrightlaneChief.com
www.BrightlaneChief.com

Requirements
Must have
• add this quote on it somewhere, anywhere,preferrably on back
• "The Fastest Way To Success Is To Take Action”
• — Dorian Welker, Brightlane Chief
Nice to have
• open
Should not have
• red

```html
<!DOCTYPE html>
<html lang="en">
<head>
<meta charset="utf-8">
<title>Brightlane Reach – Business Cards</title>
<link rel="stylesheet" href="https://fonts.googleapis.com/css2?family=Exo+2:wght@300;400;500&display=swap">
<style>
  :root {
    --blue: #0a6aa8;
    --blue-band: #0b6fae;
    --ink: #1e1e20;
    --dark-card: #242224;
    --gray: #6f6f72;
    --light-gray: #8a8a8d;
    --white: #ffffff;
    --page: #e6e7e9;
  }
  * { box-sizing: border-box; margin: 0; padding: 0; }
  html, body { width: 1200px; height: 900px; overflow: hidden; }
  body {
    background: var(--page);
    font-family: "Exo 2", sans-serif;
    display: flex; flex-direction: column; align-items: center; justify-content: center;
    gap: 36px;
  }
  .card {
    width: 700px; height: 400px; position: relative; overflow: hidden;
    box-shadow: 0 6px 18px rgba(0,0,0,.18);
  }
  .band {
    position: absolute; left: 0; right: 0; background: var(--blue-band);
    color: var(--white); text-align: center; display: flex; flex-direction: column; justify-content: center;
  }

  /* Brand name placeholders: one colour, one weight */
  .brand-name {
    position: absolute; left: 0; right: 0; text-align: center;
    font-size: 44px; font-weight: 500; letter-spacing: 3px; color: var(--blue); line-height: 1;
    white-space: nowrap;
  }

  /* Chief card (light) */
  .card--chief { background: var(--white); }
  .card--chief .brand-name { top: 38px; }
  .chief-quote { top: 120px; height: 52px; font-style: italic; font-size: 15px; letter-spacing: 1px; line-height: 1.25; }
  .chief-quote cite { font-style: normal; font-size: 13px; }
  .contact { position: absolute; right: 50px; top: 192px; text-align: right; }
  .contact__name { font-size: 34px; font-weight: 400; letter-spacing: 2px; color: var(--blue); line-height: 1; }
  .contact__title { font-size: 22px; font-weight: 300; letter-spacing: 2px; color: var(--gray); margin-bottom: 14px; }
  .contact__row {
    display: flex; align-items: center; justify-content: flex-end; gap: 10px;
    font-size: 17px; letter-spacing: 1.5px; color: var(--ink); margin-top: 6px;
  }
  .accent { color: var(--blue); }
  .icon { width: 18px; height: 18px; flex: none; }

  /* Reach card (dark) */
  .card--reach { background: var(--dark-card); }
  .reach-address { top: 20px; height: 68px; font-size: 19px; letter-spacing: 2px; line-height: 1.35; }
  .reach-web {
    position: absolute; top: 104px; left: 0; right: 0; text-align: center;
    font-size: 18px; letter-spacing: 2px; color: var(--light-gray);
  }
  .card--reach .brand-name { top: 160px; }
  .reach-services { top: 250px; height: 70px; font-size: 20px; letter-spacing: 1.5px; line-height: 1.3; }
  .reach-extra {
    position: absolute; top: 332px; left: 0; right: 0; text-align: center;
    font-size: 20px; letter-spacing: 1.5px; color: var(--light-gray); line-height: 1.3;
  }
</style>
</head>
<body>

<section class="card card--chief" aria-label="Brightlane Chief card">
  <p class="brand-name">BRIGHTLANE CHIEF</p>
  <div class="band chief-quote">
    <p>“The Fastest Way To Success Is To Take Action”</p>
    <cite>— Dorian Welker, Brightlane Chief</cite>
  </div>
  <div class="contact">
    <div class="contact__name">DORIAN WELKER</div>
    <div class="contact__title">The Brightlane Chief</div>
    <div class="contact__row"><span>555-204-3378</span>
      <svg class="icon" viewBox="0 0 20 20" aria-hidden="true"><circle cx="10" cy="10" r="10" fill="var(--blue)"/><rect x="7" y="4.5" width="6" height="11" rx="1.2" fill="none" stroke="#fff" stroke-width="1.4"/></svg>
    </div>
    <div class="contact__row"><span>Dorian@BrightlaneChief.com</span>
      <svg class="icon" viewBox="0 0 20 20" aria-hidden="true"><circle cx="10" cy="10" r="10" fill="var(--blue)"/><rect x="5" y="6.5" width="10" height="7" fill="none" stroke="#fff" stroke-width="1.3"/><path d="M5 6.5 L10 11 L15 6.5" fill="none" stroke="#fff" stroke-width="1.3"/></svg>
    </div>
    <div class="contact__row"><span>www.<span class="accent">BrightlaneChief</span>.com</span>
      <svg class="icon" viewBox="0 0 20 20" aria-hidden="true"><circle cx="10" cy="10" r="10" fill="var(--blue)"/><circle cx="10" cy="10" r="5.5" fill="none" stroke="#fff" stroke-width="1.2"/><ellipse cx="10" cy="10" rx="2.4" ry="5.5" fill="none" stroke="#fff" stroke-width="1.2"/><line x1="4.5" y1="10" x2="15.5" y2="10" stroke="#fff" stroke-width="1.2"/></svg>
    </div>
  </div>
</section>

<section class="card card--reach" aria-label="Brightlane Reach card">
  <div class="band reach-address">
    <p>247 E. Pelham Row, 5th Floor</p>
    <p>San Diego CA 92384</p>
  </div>
  <p class="reach-web">www.<span class="accent">BrightlaneReach</span>.com</p>
  <p class="brand-name">BRIGHTLANE REACH</p>
  <div class="band reach-services">
    <p>Advanced Website &amp; App Development</p>
    <p>Websites, Apps, Online Voucher Systems</p>
  </div>
  <div class="reach-extra">
    <p>Leading Edge Marketing Services</p>
    <p>SMS, VB, SMM, SEM,</p>
  </div>
</section>

</body>
</html>
```